CD-/Plattencover für Ratgeber für Patienten mit sehr starkem Übergewicht
Zielgruppe
Die Seite Leichtweg Basel ist Ratgeber für Patienten mit sehr starkem Übergewicht.
Das Team von zwei führenden Kliniken in der Adipositas Chirugie ( Klinikum Seefeldhang und Spital Rebhalden )
Stellen Ihre Kompetenz und Ihr Wissen betroffenen Patienten zur Verfügung. Ergänzt wird die Seite durch einen Podcast.
Der Waagfunk ist der Podcast für stark übergewichtige Zuhörer. Interviews mit Chirugen, Ernährungsberatern und anderen Experten helfen betroffenen Patienten bei der Entscheidung einer Operation (Magenverkleinerung) Die Hosts des Podcast sind drei Experten Prof. Dr. med. Lukas Ferrand, PD Dr. med. Severin Morgental und Ilyas Korvani.
Um das Cover dieses Podcast geht es bei diesem Auftrag. Die Zuhörer kommen überwiegend aus Deutschland,Österreich und der Schweiz.
Aufgabenstellung
Es sollte eines der beiden beigefügten Fotos der drei Hosts sowie das beigefügte Logo von Leichtweg Basel verwendet werden. Außerdem sollte das Cover den Begriff Waagfunk und den Slogan
Der Kanal für Menschen mit starkem Übergewicht
beinhalten. Farben, Schrift und zusätzliche Gestaltungselemente sind frei wählbar. Ich freue mich auf Ihre Vorschläge.

```html
<!DOCTYPE html>
<html lang="de">
<head>
<meta charset="utf-8">
<title>Waagfunk – Podcast-Cover</title>
<link rel="stylesheet" href="https://fonts.googleapis.com/css2?family=Source+Serif+4:opsz,wght@8..60,400;8..60,600;8..60,700&family=Cabin:wght@400&display=swap">
<style>
  :root {
    --board-bg: #f7f6f1;
    --cover-bg: #ede6d7;
    --accent: #e84e1b;
    --ink: #2e2e2e;
    --ink-soft: #4a4a4a;
  }
  * { margin: 0; padding: 0; box-sizing: border-box; }
  html, body { width: 1200px; height: 1200px; overflow: hidden; }
  body {
    background: var(--board-bg);
    font-family: "Source Serif 4", Georgia, serif;
    color: var(--ink);
    position: relative;
  }
  .cover {
    position: absolute;
    left: 289px; top: 88px;
    width: 620px; height: 619px;
    background: var(--cover-bg);
    box-shadow: 0 6px 18px rgba(0,0,0,0.12);
    overflow: hidden;
  }
  .title {
    position: absolute;
    right: 232px; top: 116px;
    text-align: right;
    color: var(--accent);
    font-weight: 600;
    font-size: 80px;
    line-height: 66px;
    letter-spacing: -1px;
  }
  .slogan {
    position: absolute;
    right: 236px; top: 250px;
    text-align: right;
    font-size: 23px;
    line-height: 31px;
    color: var(--ink-soft);
  }
  .badge {
    position: absolute;
    left: 445px; top: 34px;
    width: 140px; height: 140px;
    border-radius: 50%;
    background: var(--accent);
  }
  .brand {
    position: absolute;
    left: 350px; top: 325px;
    display: flex; align-items: center; gap: 8px;
    font-weight: 700;
    font-size: 22px;
    color: var(--accent);
  }
  .brand-dot { width: 14px; height: 14px; background: var(--ink); }
  .host-photo {
    position: absolute;
    left: 1px; top: 362px;
    width: 619px; height: 204px;
    background: linear-gradient(180deg, #a9acab 0%, #c9c6bb 28%, #8e8a5a 55%, #5d5a2e 80%, #3b3520 100%);
  }
  .hosts-caption {
    position: absolute;
    left: 0; right: 0; top: 587px;
    text-align: center;
    font-family: "Cabin", Arial, sans-serif;
    font-size: 13px;
    color: var(--ink-soft);
  }
  .intro {
    position: absolute;
    left: 70px; top: 756px;
    width: 1060px;
    text-align: center;
    font-size: 16.2px;
    line-height: 23px;
  }
  .intro p + p { margin-top: 23px; }
</style>
</head>
<body>
  <section class="cover">
    <h1 class="title">WAAG<br>FUNK</h1>
    <p class="slogan">Der Kanal für Menschen mit<br>starkem Übergewicht</p>
    <div class="badge" role="img" aria-label="Runde Plakette mit Waage-Symbol und Lebensmittel-Icons"></div>
    <div class="brand"><span class="brand-dot"></span>Leichtweg Basel</div>
    <div class="host-photo" role="img" aria-label="Foto der drei Hosts auf einer Terrasse über einem See im Herbst"></div>
    <p class="hosts-caption">PROF. DR. MED. LUKAS FERRAND, PD DR. MED. SEVERIN MORGENTAL UND ILYAS KORVANI.</p>
  </section>

  <div class="intro">
    <p>Willkommen beim Waagfunk, dem Podcast für Menschen mit starkem<br>Übergewicht. Wir bieten Ihnen Interviews mit führenden Chirurgen,<br>Ernährungsberatern und anderen Experten, um Ihnen bei der Entscheidung einer Operation zur Gewichtsreduktion zu helfen. Als<br>Teil der Seite Leichtweg Basel, einer Informationsplattform für Patienten mit starkem Übergewicht, sind wir bestrebt, Ihnen das<br>Wissen und die Kompetenz von zwei führenden Kliniken in der Adipositas Chirurgie, dem Klinikum Seefeldhang und dem<br>Spital Rebhalden, zur Verfügung zu stellen.</p>
    <p>Unsere Hosts sind drei Experten auf dem Gebiet der Adipositas-Chirurgie:<br>Prof. Dr. med. Lukas Ferrand, PD Dr. med. Severin Morgental und Ilyas Korvani. Gemeinsam bringen sie jahrzehntelange Erfah-<br>rung in der Betreuung von Patienten mit starkem Übergewicht mit.<br>Unser Fokus liegt auf der Aufklärung und Unterstützung von Menschen mit starkem Übergewicht, die sich für eine Operation zur<br>Gewichtsreduktion entscheiden möchten. Wir besprechen verschiedene Arten von Gewichtsverlustoperationen, einschließlich der<br>Magenverkleinerung, und bieten umfassende Informationen und Ratschläge, damit Sie eine fundierte Entscheidung treffen können.</p>
    <p>Wir freuen uns darauf, Ihnen zu helfen, Ihr Leben durch Gewichtsverlust und eine verbesserte Gesundheit zu transformieren. Der<br>Waagfunk ist für Zuhörer aus Deutschland, Österreich und der Schweiz verfügbar. Bleiben Sie dran und erfahren Sie mehr über die<br>Möglichkeiten zur Gewichtsreduktion.</p>
  </div>
</body>
</html>
```